Professional / Luxury Rack Card Design Needed (Do not use AI)

We are a private, boutique style optometry practice in College Station, Texas. We want the new design to communicate a premium, modern, luxury eye care experience while remaining professional and approachable.
When someone picks up this rack card, we want them to think:
"This practice looks modern, advanced, trustworthy, and premium. I would expect exceptional care and a high-end eyewear experience."

Target Market(s)

Families, professionals, adults seeking comprehensive medical eye care and vision correction. Patients seeking premium eyewear, advanced technology, and personalize care. Individuals and families seeking long term relationships with a trusted eye care provider. Patients who value exceptional service, expertise, and convenience.

Industry/Entity Type

Medical & Optometry-luxury optical

Font styles to use
Serif
Other font styles liked:
• Avenir if available. If not, Montserrat for headlines and Open Sans for Body text. For the slogan, use larger bold Montserrat.

Requirements
Must have
• Non-edited photo of doctors (merged together) with names. "Your Vision. Our Focus." Phone, website, Text/Call to Schedule appointment (Call to action to schedule). Accepting new patients. Eye Care center logo prominently displayed. Real photo of Eye Care Center building. Contact information (see attachement with all info)
Nice to have
• For frame brands, use the branded names. (see attachment)
Should not have
• Shouild not be busy/cluttered. Do not use scripted font from my website. Do NOT use AI generated images. Do not edit doctor faces other than merging them together. DO NOT use AI to edit faces....only to merge them side by side.

```html
<!DOCTYPE html>
<html lang="en">
<head>
<meta charset="utf-8">
<title>Clearview Optical Rack Card</title>
<link href="https://fonts.googleapis.com/css2?family=Playfair+Display:wght@700;900&family=Mulish:wght@300;400;600;700&display=swap" rel="stylesheet">
<style>
  :root {
    --navy: #1e3549;
    --gold: #dfb50e;
    --white: #ffffff;
    --paper: #f4f4f4;
    --stage: #d9d9d9;
    --ink: #2a2a2a;
    --grey: #7b7f84;
  }
  * { box-sizing: border-box; margin: 0; padding: 0; }
  html, body { width: 725px; height: 1200px; overflow: hidden; background: var(--stage); }
  body { position: relative; font-family: "Mulish", "Open Sans", sans-serif; }
  .card { position: absolute; top: 218px; width: 340px; height: 765px; background: var(--navy); overflow: hidden; }
  .card--front { left: 15px; }
  .card--back { left: 370px; }
  .abs { position: absolute; }

  /* Front */
  .logo-tab { left: 38px; top: 0; width: 265px; height: 70px; background: var(--white); border-radius: 0 0 18px 18px; display: flex; align-items: center; justify-content: center; gap: 10px; }
  .logo-tab__mark { width: 26px; height: 26px; border-radius: 50%; background: var(--grey); flex: none; }
  .logo-tab__text { display: flex; flex-direction: column; }
  .logo-tab__name { font-size: 23px; font-weight: 300; color: var(--grey); line-height: 1; }
  .logo-tab__member { font-size: 7px; font-weight: 300; color: var(--grey); letter-spacing: 1.5px; margin-top: 4px; text-transform: uppercase; }
  .headline { left: 0; top: 90px; width: 340px; text-align: center; font-family: "Playfair Display", "Times New Roman", serif; font-weight: 900; font-size: 58px; line-height: 63px; letter-spacing: 1px; }
  .headline span { display: block; }
  .headline .is-white { color: var(--white); }
  .headline .is-gold { color: var(--gold); }
  .highlights { left: 33px; top: 361px; width: 274px; height: 330px; background: var(--gold); border-radius: 17px 17px 0 0; padding: 14px 0 0 16px; list-style: none; }
  .highlights li { font-size: 19px; color: var(--navy); line-height: 36px; font-weight: 400; padding-left: 14px; position: relative; }
  .highlights li::before { content: ""; position: absolute; left: 0; top: 16px; width: 6px; height: 6px; border-radius: 50%; background: var(--navy); }
  .highlights li.wrap { line-height: 27px; padding-top: 4px; }
  .highlights li.wrap::before { top: 16px; }
  .highlights strong { font-weight: 700; }
  .building-photo { left: 0; top: 560px; width: 340px; height: 170px; background: linear-gradient(180deg, #c8b79a 0%, #a88f6b 55%, #5d4a36 100%); clip-path: polygon(0 22%, 20% 10%, 40% 4%, 60% 0, 80% 8%, 100% 14%, 100% 100%, 0 100%); }
  .contact-bar { left: 15px; top: 717px; width: 309px; height: 38px; background: var(--gold); border-radius: 4px; display: flex; justify-content: space-around; align-items: center; padding: 0 6px; }
  .contact-bar__item { display: flex; flex-direction: column; align-items: center; gap: 3px; font-size: 9.5px; color: var(--navy); }
  .contact-bar__item svg { width: 9px; height: 9px; fill: var(--navy); }

  /* Back */
  .doctor-band { left: 0; width: 340px; height: 94px; background: var(--gold); }
  .doctor-photo { width: 94px; height: 94px; border-radius: 50%; background: radial-gradient(circle at 50% 70%, #efefef 0 30%, #9c8a74 60%, #7b6a58 100%); box-shadow: 0 4px 0 var(--white); }
  .doctor-name { width: 120px; text-align: center; color: var(--white); font-size: 9.5px; font-weight: 700; line-height: 12px; }
  .service-title { left: 0; top: 303px; width: 340px; display: flex; align-items: center; justify-content: center; gap: 6px; font-family: "Playfair Display", "Times New Roman", serif; font-weight: 700; font-size: 19px; color: var(--gold); letter-spacing: 1px; }
  .service-title::before, .service-title::after { content: ""; width: 40px; height: 1px; background: var(--gold); }
  .service { display: flex; gap: 5px; font-size: 10px; line-height: 12.5px; color: var(--white); width: 150px; }
  .service__num { flex: none; width: 10px; height: 10px; border: 1px solid var(--gold); border-radius: 50%; font-size: 5.5px; color: var(--white); display: flex; align-items: center; justify-content: center; margin-top: 1px; }
  .brands { left: 0; top: 521px; width: 340px; height: 153px; background: var(--paper); }
  .brand { width: 90px; text-align: center; font-size: 10.5px; color: var(--ink); transform: translateX(-50%); }
  .brand--spaced { letter-spacing: 3px; font-weight: 400; }
  .brand--bold { font-weight: 700; letter-spacing: 1px; }
  .brand--more { color: var(--navy); font-weight: 700; font-size: 9px; letter-spacing: 1.5px; }
  .info-box { left: 20px; top: 685px; width: 301px; height: 65px; background: var(--gold); border-radius: 7px; display: flex; padding: 9px 10px; gap: 10px; }
  .info-box__col h3 { font-size: 10px; font-weight: 700; color: var(--navy); margin-bottom: 5px; }
  .info-box__col p { font-size: 6px; line-height: 8px; color: var(--navy); }
</style>
</head>
<body>

<section class="card card--front" aria-label="Rack card front">
  <div class="abs logo-tab">
    <span class="logo-tab__mark"></span>
    <span class="logo-tab__text">
      <span class="logo-tab__name">Clearview Optical</span>
      <span class="logo-tab__member">A member of Optic Alliance</span>
    </span>
  </div>
  <h1 class="abs headline">
    <span class="is-white">YOUR</span>
    <span class="is-gold">VISION.</span>
    <span class="is-white">OUR</span>
    <span class="is-gold">FOCUS.</span>
  </h1>
  <ul class="abs highlights">
    <li>Comprehensive Eye Care</li>
    <li>Advanced Technology</li>
    <li>Personalized Care</li>
    <li class="wrap">Over <strong>1,000</strong> Designer<br>Frames &amp; Sunglasses</li>
  </ul>
  <div class="abs building-photo" role="img" aria-label="Photo of the practice building exterior"></div>
  <div class="abs contact-bar">
    <div class="contact-bar__item">
      <svg viewBox="0 0 24 24"><path d="M6.6 10.8a15 15 0 0 0 6.6 6.6l2.2-2.2a1 1 0 0 1 1-.25 11.4 11.4 0 0 0 3.6.57 1 1 0 0 1 1 1V20a1 1 0 0 1-1 1A17 17 0 0 1 3 4a1 1 0 0 1 1-1h3.5a1 1 0 0 1 1 1c0 1.25.2 2.45.57 3.57a1 1 0 0 1-.25 1z"/></svg>
      <span>(555) 214-3800</span>
    </div>
    <div class="contact-bar__item">
      <svg viewBox="0 0 24 24"><path d="M6.6 10.8a15 15 0 0 0 6.6 6.6l2.2-2.2a1 1 0 0 1 1-.25 11.4 11.4 0 0 0 3.6.57 1 1 0 0 1 1 1V20a1 1 0 0 1-1 1A17 17 0 0 1 3 4a1 1 0 0 1 1-1h3.5a1 1 0 0 1 1 1c0 1.25.2 2.45.57 3.57a1 1 0 0 1-.25 1z"/></svg>
      <span>(555) 214-3811</span>
    </div>
    <div class="contact-bar__item">
      <svg viewBox="0 0 24 24"><circle cx="12" cy="12" r="10" fill="none" stroke="#1e3549" stroke-width="2"/><ellipse cx="12" cy="12" rx="4" ry="10" fill="none" stroke="#1e3549" stroke-width="2"/><path d="M2 12h20" stroke="#1e3549" stroke-width="2"/></svg>
      <span>ClearviewOptical.com</span>
    </div>
  </div>
</section>

<section class="card card--back" aria-label="Rack card back">
  <div class="abs doctor-band" style="top:20px"></div>
  <div class="abs doctor-band" style="top:155px"></div>

  <div class="abs doctor-photo" style="left:67px;top:20px" role="img" aria-label="Portrait of Dr. Laura Whitfield"></div>
  <div class="abs doctor-photo" style="left:177px;top:20px" role="img" aria-label="Portrait of Dr. Megan Caldwell"></div>
  <p class="abs doctor-name" style="left:54px;top:120px">Dr. Laura Whitfield,<br>O.D</p>
  <p class="abs doctor-name" style="left:164px;top:120px">Dr. Megan Caldwell,<br>O.D</p>

  <div class="abs doctor-photo" style="left:67px;top:155px" role="img" aria-label="Portrait of Dr. Elena Marsh"></div>
  <div class="abs doctor-photo" style="left:177px;top:155px" role="img" aria-label="Portrait of Dr. Nora Bellamy"></div>
  <p class="abs doctor-name" style="left:54px;top:257px">Dr. Elena Marsh,<br>O.D.</p>
  <p class="abs doctor-name" style="left:164px;top:257px">Dr. Nora Bellamy,<br>O.D</p>

  <h2 class="abs service-title">OUR SERVICE</h2>

  <div class="abs service" style="left:32px;top:338px"><span class="service__num">1</span><span>Comprehensive<br>Eye Exams</span></div>
  <div class="abs service" style="left:187px;top:338px"><span class="service__num">2</span><span>Dry Eye &amp;<br>Allergy</span></div>
  <div class="abs service" style="left:32px;top:376px"><span class="service__num">3</span><span>Speciality Contact<br>Lens Service</span></div>
  <div class="abs service" style="left:187px;top:376px"><span class="service__num">4</span><span>Migraine &amp;<br>Headache</span></div>
  <div class="abs service" style="left:32px;top:414px"><span class="service__num">5</span><span>Pediatric Exams</span></div>
  <div class="abs service" style="left:187px;top:414px"><span class="service__num">6</span><span>Eye Muscle Alignment</span></div>
  <div class="abs service" style="left:32px;top:439px"><span class="service__num">7</span><span>Surgery Co<br>Management</span></div>
  <div class="abs service" style="left:187px;top:439px"><span class="service__num">8</span><span>Eye Injuries &amp;<br>Infections</span></div>
  <div class="abs service" style="left:32px;top:477px"><span class="service__num">9</span><span>Cataract, Glaucoma,<br>Macular Degeneration</span></div>
  <div class="abs service" style="left:187px;top:477px"><span class="service__num">10</span><span>Ocular Disease<br>Management</span></div>

  <div class="abs brands">
    <span class="abs brand brand--spaced" style="left:77px;top:14px">AURELIO</span>
    <span class="abs brand" style="left:164px;top:12px">lila rowe</span>
    <span class="abs brand brand--bold" style="left:251px;top:14px">MARVENO</span>
    <span class="abs brand" style="left:77px;top:46px">CRYSTELLE</span>
    <span class="abs brand" style="left:164px;top:46px">Airline</span>
    <span class="abs brand" style="left:251px;top:46px">HARTWELL &amp; CO.</span>
    <span class="abs brand brand--bold" style="left:77px;top:77px">VANCE ELLIS</span>
    <span class="abs brand brand--spaced" style="left:164px;top:77px">SOLENNE</span>
    <span class="abs brand brand--bold" style="left:251px;top:77px">TIDEWATER</span>
    <span class="abs brand brand--bold" style="left:77px;top:109px">RIDGEBACK</span>
    <span class="abs brand" style="left:164px;top:109px">Sunward</span>
    <span class="abs brand" style="left:251px;top:109px">Kailua</span>
    <span class="abs brand brand--more" style="left:170px;top:136px">&amp; MORE</span>
  </div>

  <div class="abs info-box">
    <div class="info-box__col" style="width:108px">
      <h3>GET IN TOUCH</h3>
      <p>(555) 214-3800<br>hello@clearviewoptical.com<br>www.clearviewoptical.com</p>
    </div>
    <div class="info-box__col" style="width:105px">
      <h3>ADDRESS</h3>
      <p>412 LUMEN WAY, SUITE 110,<br>BROOKFIELD, ST 54321</p>
    </div>
    <div class="info-box__col">
      <h3>HOURS</h3>
      <p>M-F: 8AM-6PM<br>SAT: 9AM-3PM<br>SUN: CLOSED</p>
    </div>
  </div>
</section>

</body>
</html>
```